Event Production Company needs a Poster for a karaoke party

We need a poster similar to the one attached (the same typology of the logo), in which it can be seen that there are three prizes for the winners, a presenter and a jury. The room where the party is held is in Verul next Saturday, December 17, 2022. We are looking for an innovative poster, with a youthful air and a desire to party
Target Market(s)
Young people between 16 and 20 years old
Other font styles liked:
- Pump Triline

Colors
E54698
E96AAD
F1A4CE
F9D9EA
FCEFF6
A7469A
B969AE
D3A5CF
EDDBEB
F8F0F9
6B429C
8869AF
B7A5CE
E3DAEB
F3F0F8
Requirements
Must have
- Fluorescent colors (neon), date, time and day of the event, the instagram profile has to appear

Nice to have
- that the gifts that are offered appear

Should not have
- little relevant information

```html
<!DOCTYPE html>
<html lang="es">
<head>
<meta charset="utf-8">
<title>Vibe Karaoke – Poster</title>
<link href="https://fonts.googleapis.com/css2?family=Monoton&family=Bebas+Neue&family=Josefin+Sans:wght@300;400&family=Poppins:wght@400;600&display=swap" rel="stylesheet">
<style>
  :root {
    --bg-deep: #12061a;
    --bg-mid: #2a1230;
    --neon-cyan: #45d9f2;
    --neon-purple: #b44cf0;
    --neon-violet: #8a3ff0;
    --neon-pink: #e54698;
    --pink-soft: #e96aad;
    --neon-yellow: #f3e45a;
    --text-white: #f8f0f9;
    --text-lilac: #d3a5cf;
  }
  * { margin: 0; padding: 0; box-sizing: border-box; }
  html, body { width: 750px; height: 1200px; overflow: hidden; background: var(--bg-deep); }
  .poster {
    position: relative; width: 750px; height: 1200px; overflow: hidden;
    background:
      radial-gradient(ellipse 70% 45% at 50% 38%, rgba(120, 40, 60, .45), transparent 70%),
      radial-gradient(ellipse 90% 60% at 50% 60%, var(--bg-mid), var(--bg-deep) 80%);
    font-family: "Poppins", sans-serif; color: var(--text-white);
  }
  .abs { position: absolute; }

  .client-name {
    left: 0; width: 100%; top: 62px; text-align: center;
    font-family: "Poppins", sans-serif; font-weight: 600; color: var(--neon-purple);
    font-size: 42px; line-height: 50px;
  }
  .client-city {
    left: 0; width: 100%; top: 166px; text-align: center;
    font-family: "Poppins", sans-serif; font-weight: 600; font-size: 15px; letter-spacing: 5px;
    color: var(--neon-purple);
  }

  .neon-frame { left: 0; top: 0; width: 750px; height: 1200px; pointer-events: none; }

  .event-name {
    left: 0; width: 100%; top: 262px; text-align: center;
    font-family: "Poppins", sans-serif; font-weight: 600; font-size: 150px; line-height: 180px;
    color: var(--neon-purple);
  }
  .event-sub {
    left: 0; width: 100%; top: 450px; text-align: center;
    font-family: "Josefin Sans", sans-serif; font-weight: 300;
    font-size: 58px; letter-spacing: 12px; color: var(--text-white);
  }

  .mic-art {
    left: 185px; top: 525px; width: 480px; height: 185px; border-radius: 92px;
    background: radial-gradient(ellipse at 70% 40%, rgba(233, 106, 173, .55), rgba(229, 70, 152, .18) 60%, transparent 75%);
  }
  .gifts-art {
    left: 60px; top: 735px; width: 355px; height: 195px; border-radius: 30px;
    background: linear-gradient(90deg, rgba(200, 200, 210, .25), rgba(90, 70, 240, .45) 45%, rgba(214, 70, 200, .4));
  }

  .date-year {
    left: 463px; top: 800px; width: 130px; transform: rotate(-90deg);
    font-family: "Josefin Sans", sans-serif; font-weight: 300; font-size: 60px;
    letter-spacing: 6px; color: var(--neon-pink); line-height: 60px; text-align: center;
  }
  .date-month {
    left: 568px; top: 736px; font-family: "Bebas Neue", sans-serif;
    font-size: 36px; letter-spacing: 2px; color: var(--text-white);
  }
  .date-day {
    left: 560px; top: 762px; font-family: "Monoton", cursive;
    font-size: 128px; line-height: 150px; color: var(--neon-violet);
  }
  .date-time {
    left: 498px; top: 913px; width: 197px; display: flex; align-items: center; gap: 6px;
    font-family: "Poppins", sans-serif; font-size: 19px; color: var(--neon-yellow);
  }
  .date-time::before, .date-time::after { content: ""; flex: 1; height: 0; border-top: 3px double var(--neon-pink); }

  .host-label { left: 58px; top: 966px; font-size: 13px; color: var(--neon-purple); }
  .host-names {
    left: 58px; top: 982px; font-family: "Bebas Neue", sans-serif;
    font-size: 44px; line-height: 44px; color: var(--text-white);
  }
  .host-jury {
    left: 58px; top: 1026px; font-family: "Josefin Sans", sans-serif;
    font-size: 23px; letter-spacing: 2px; color: var(--neon-cyan);
  }

  .prize-total {
    left: 445px; top: 968px; font-family: "Monoton", cursive;
    font-size: 50px; line-height: 64px; color: var(--neon-cyan);
  }
  .prize-label {
    left: 632px; top: 982px; font-family: "Bebas Neue", sans-serif;
    font-size: 22px; line-height: 22px; color: var(--neon-yellow);
  }

  .info-label { left: 58px; top: 1078px; font-size: 17px; color: var(--text-white); }
  .social {
    left: 58px; top: 1100px; display: flex; align-items: center; gap: 6px;
    font-size: 30px; font-weight: 600; color: var(--neon-purple);
  }
  .social-dot { width: 28px; height: 28px; border-radius: 50%; border: 3px solid var(--pink-soft); }

  .venue {
    right: 55px; top: 1098px; font-size: 33px; color: var(--text-white);
  }
  .venue-name { color: var(--neon-pink); }
</style>
</head>
<body>
<main class="poster">
  <header>
    <div class="abs client-name">Cantos<br>Rooms</div>
    <div class="abs client-city">GIRONA</div>
  </header>

  <svg class="abs neon-frame" viewBox="0 0 750 1200" aria-hidden="true">
    <defs>
      <filter id="glow" x="-20%" y="-20%" width="140%" height="140%">
        <feGaussianBlur stdDeviation="7" result="b"/>
        <feMerge><feMergeNode in="b"/><feMergeNode in="b"/><feMergeNode in="SourceGraphic"/></feMerge>
      </filter>
    </defs>
    <path d="M200 472 H80 Q66 472 66 458 V258 Q66 244 80 244 H680 Q694 244 694 258 V458 Q694 472 680 472 H570"
          fill="none" stroke="var(--neon-cyan)" stroke-width="7" stroke-linecap="round" filter="url(#glow)"/>
    <path d="M200 472 H80 Q66 472 66 458 V258 Q66 244 80 244 H680 Q694 244 694 258 V458 Q694 472 680 472 H570"
          fill="none" stroke="#d9f7fc" stroke-width="2.5" stroke-linecap="round"/>
  </svg>

  <h1>
    <span class="abs event-name">Vibe</span>
    <span class="abs event-sub">KARAOKE</span>
  </h1>

  <div class="abs mic-art" role="img" aria-label="Neon pink microphone with a looping cable and a +16 party sign"></div>
  <div class="abs gifts-art" role="img" aria-label="Three neon gift boxes tagged 1st 300€, 2nd 150€ and 3rd 50€"></div>

  <section class="event-date">
    <div class="abs date-year">2022</div>
    <div class="abs date-month">DECEMBER</div>
    <div class="abs date-day">17</div>
    <div class="abs date-time">19:00H</div>
  </section>

  <section class="hosts">
    <div class="abs host-label">PRESENTADO POR</div>
    <div class="abs host-names">NURIA LLEÓ Y CARLA MIR</div>
    <div class="abs host-jury">JURADO PROFESIONAL</div>
  </section>

  <section class="prizes">
    <div class="abs prize-total">+1000</div>
    <div class="abs prize-label">EN<br>PREMIOS</div>
  </section>

  <footer>
    <div class="abs info-label">Toda la info</div>
    <div class="abs social"><span class="social-dot"></span>@vibekaraoke</div>
    <div class="abs venue">VENUE: <span class="venue-name">VERUL</span></div>
  </footer>
</main>
</body>
</html>
```